Website for Fashion/Jewelry online seller

We would like a website design that can be used in wordpress. It will be important to be able to link instagram, twitter, etc posts on the bottom of site. We are to be a online seller of chic jewelry, art, fashion, and other home design industries. Currently we emphasize jewelry but as the years move forward, other products will be introduced as collections in home furnishings and primarily women's fashion. It will be important to have a “shop now” section where people can order products online so ecommerce will need to be set up at some point. The website should have the following feel: clean, modern, contemporary and chic. A lot of whites should be used with simple text and simple but elegant fonts. Best is to go to mirevatolkin.example to get the best idea of what we are wanting for the look and feel of the site.

Target Market(s)

upper social class people that are into fashion, jewelry, etc

Industry/Entity Type

Fashion

Number of Pages Required

5+ page

Font styles to use
Other font styles liked:
• go to karodwen.example to see the font desired

Requirements
Must have
• Name of Company is Tide Harbor 7
Nice to have
• see project description
Should not have
• see project description

```html
<!DOCTYPE html>
<html lang="en">
<head>
<meta charset="utf-8">
<title>Tide Harbor 7 — Jewelry &amp; Fashion</title>
<link href="https://fonts.googleapis.com/css2?family=Jost:ital,wght@0,300;0,400;0,500;1,300;1,400&family=Crimson+Text:wght@400;600&display=swap" rel="stylesheet">
<style>
:root{
  --accent:#fd7446;
  --ink:#222;
  --topbar:#000;
  --line:#e3e3e3;
  --card:#f4f4f4;
  --band:#efefef;
  --footer:#333;
  --footer-base:#232323;
  --tag-dark:#444;
  --white:#fff;
}
*{margin:0;padding:0;box-sizing:border-box}
html,body{width:1200px;height:2663px;overflow:hidden;background:var(--white)}
body{position:relative;font-family:"Jost",sans-serif;color:var(--ink)}
.abs{position:absolute}

/* top bar */
.topbar{left:0;top:0;width:1200px;height:75px;background:var(--topbar);color:var(--white)}
.brand{left:85px;top:16px;font-size:32px;font-weight:400;letter-spacing:.5px;white-space:nowrap}
.search{left:360px;top:27px;font-family:"Crimson Text",serif;font-size:15px;color:#8a8a8a;display:flex;align-items:center;gap:10px}
.topdiv{top:0;width:1px;height:75px;background:#2b2b2b}
.topicon{top:28px}
.cart{left:952px;top:27px;display:flex;gap:26px;align-items:center;font-family:"Crimson Text",serif;font-size:15px;color:#9a9a9a}

/* nav */
.nav{left:0;top:75px;width:1200px;height:40px;border-bottom:1px solid var(--line)}
.nav-item{top:0;height:40px;display:flex;align-items:center;justify-content:center;gap:10px;font-family:"Crimson Text",serif;font-size:14px;letter-spacing:1px;color:#444;border-left:1px solid var(--line)}
.nav-item.last{border-right:1px solid var(--line)}

/* hero */
.hero{left:0;top:115px;width:1200px;height:533px;overflow:hidden;
  background:linear-gradient(100deg,#e4ddd6 0%,#f1ede9 40%,#f9f7f5 70%,#fbfaf9 100%)}
.hero-bride{left:60px;top:0;width:470px;height:533px;
  background:
    radial-gradient(ellipse 70px 85px at 52% 22%,#d8c3b2 0%,#d8c3b2 55%,rgba(216,195,178,0) 100%),
    radial-gradient(ellipse 150px 200px at 50% 72%,#fbfaf8 0%,#f3efeb 60%,rgba(243,239,235,0) 100%),
    radial-gradient(ellipse 60px 60px at 50% 16%,#6d5646 0%,rgba(109,86,70,0) 100%),
    linear-gradient(180deg,#e6ddd5,#efe9e4)}
.hero-rings{left:410px;top:270px;width:500px;height:260px;
  background:
    radial-gradient(ellipse 110px 70px at 28% 62%,#e8e3df 0%,#b9aea6 45%,rgba(185,174,166,0) 75%),
    radial-gradient(ellipse 90px 80px at 50% 40%,#d6cec8 0%,#a99d94 45%,rgba(169,157,148,0) 75%),
    radial-gradient(ellipse 90px 90px at 80% 42%,#ebe6e2 0%,#b3a79e 45%,rgba(179,167,158,0) 75%)}
.hero-title{left:560px;top:76px;width:580px;text-align:center;color:var(--accent);font-size:42px;font-weight:300;letter-spacing:1px;white-space:nowrap}
.hero-sub{left:560px;top:141px;width:580px;text-align:center;font-size:30px;font-weight:400;color:#111;white-space:nowrap}
.btn-hero{left:740px;top:205px;width:218px;height:47px;background:var(--accent);color:var(--white);font-size:25px;display:flex;align-items:center;justify-content:center;letter-spacing:.5px}
.dot{left:1102px;width:12px;height:12px;border-radius:50%;background:var(--accent)}
.dot.on{background:#000}

/* section heading */
.sec-title{left:0;width:1200px;text-align:center;font-size:24px;font-weight:400;letter-spacing:.5px;color:#222}
.ornament{left:495px;width:210px;height:20px}

/* product cards */
.card-img{width:316px;height:455px;background:var(--card)}
.tag{width:68px;height:24px;color:var(--white);font-size:13px;display:flex;align-items:center;justify-content:center;border-radius:0 0 14px 14px}
.tag.orange{background:var(--accent)}
.tag.dark{background:var(--tag-dark)}
.card-name{width:316px;text-align:center;font-size:14px;color:#222}
.card-price{width:316px;text-align:center;font-family:"Crimson Text",serif;font-size:13px;color:#333}
.card-btn{width:94px;height:27px;background:var(--accent);color:var(--white);font-size:11px;display:flex;align-items:center;justify-content:center}
.arrow{width:27px;height:28px;background:#444;display:flex;align-items:center;justify-content:center}

/* promo banners */
.promo{top:1363px;height:195px;background:#f2f2f2}
.promo-img{top:0;left:0;width:200px;height:195px}
.promo-kicker{left:229px;top:42px;font-size:20px;letter-spacing:.5px;color:#222}
.promo-big{left:229px;top:70px;font-size:42px;font-weight:300;color:var(--accent);letter-spacing:1px;white-space:nowrap}
.promo-small{left:229px;top:126px;font-size:20px;color:#222;letter-spacing:.5px}

/* features */
.features{left:0;top:2265px;width:1200px;height:103px;background:var(--band)}
.feat-text{top:36px;font-size:24px;font-weight:300;color:var(--accent);letter-spacing:.3px;white-space:nowrap}
.feat-div{left:621px;top:22px;width:1px;height:60px;background:#cfcfcf}

/* footer */
.footer{left:0;top:2368px;width:1200px;height:241px;background:var(--footer);color:var(--white)}
.f-head{top:30px;font-size:20px;font-style:italic;font-weight:300}
.f-list{top:72px;list-style:none;font-family:"Crimson Text",serif;font-size:14px;font-weight:600;line-height:32px;white-space:nowrap}
.f-note{left:872px;top:74px;width:230px;font-family:"Crimson Text",serif;font-size:13px;font-weight:600;line-height:16px}
.f-input{left:872px;top:131px;width:184px;height:34px;background:var(--white);color:#555;font-family:"Crimson Text",serif;font-size:14px;padding:8px 10px}
.f-send{left:1056px;top:131px;width:47px;height:34px;background:var(--accent);display:flex;align-items:center;justify-content:center}
.base{left:0;top:2609px;width:1200px;height:54px;background:var(--footer-base);color:var(--white)}
.copy{left:98px;top:19px;font-size:12px;letter-spacing:.5px}
.social{top:16px;width:22px;height:22px;border-radius:50%;background:var(--white)}
</style>
</head>
<body>

<!-- top bar -->
<header class="abs topbar">
  <div class="abs brand">TIDE HARBOR 7</div>
  <div class="abs topdiv" style="left:338px"></div>
  <div class="abs search">
    <svg width="16" height="16" viewBox="0 0 16 16"><circle cx="6.5" cy="6.5" r="5" fill="none" stroke="#8a8a8a" stroke-width="1.6"/><line x1="10.2" y1="10.2" x2="14.5" y2="14.5" stroke="#8a8a8a" stroke-width="1.8"/></svg>
    Search Here
  </div>
  <div class="abs topdiv" style="left:680px"></div>
  <svg class="abs topicon" style="left:735px" width="14" height="16" viewBox="0 0 14 16"><circle cx="7" cy="4.5" r="3.5" fill="#9a9a9a"/><path d="M1 15c0-4 2.7-6 6-6s6 2 6 6z" fill="#9a9a9a"/></svg>
  <div class="abs topdiv" style="left:804px"></div>
  <svg class="abs topicon" style="left:855px" width="16" height="16" viewBox="0 0 16 16"><circle cx="8" cy="8" r="5" fill="none" stroke="#9a9a9a" stroke-width="3" stroke-dasharray="2.6 1.3"/><circle cx="8" cy="8" r="2.5" fill="#9a9a9a"/></svg>
  <div class="abs topdiv" style="left:920px"></div>
  <div class="abs cart">
    <svg width="16" height="15" viewBox="0 0 16 15"><path d="M0 1h3l2 8h8l2-6H4.5" fill="none" stroke="#9a9a9a" stroke-width="1.6"/><circle cx="6" cy="13" r="1.5" fill="#9a9a9a"/><circle cx="12" cy="13" r="1.5" fill="#9a9a9a"/></svg>
    <span>0 items - $00.00</span>
  </div>
</header>

<!-- navigation -->
<nav class="abs nav">
  <div class="abs nav-item" style="left:87px;width:156px">
    <svg width="20" height="17" viewBox="0 0 20 17"><path d="M10 1 1 9h3v7h4v-5h4v5h4V9h3z" fill="#333"/></svg>HOME</div>
  <div class="abs nav-item" style="left:243px;width:151px">
    <svg width="18" height="17" viewBox="0 0 18 17"><rect x="1" y="1" width="16" height="5" fill="#333"/><rect x="2" y="7" width="14" height="9" fill="none" stroke="#333" stroke-width="2"/><rect x="6" y="10" width="4" height="6" fill="#333"/></svg>SHOP</div>
  <div class="abs nav-item" style="left:394px;width:162px">
    <svg width="20" height="17" viewBox="0 0 20 17"><circle cx="8" cy="5" r="4" fill="#333"/><path d="M1 17c0-5 3-7 7-7s7 2 7 7z" fill="#333"/><circle cx="15" cy="5" r="3" fill="#333"/></svg>ABOUT</div>
  <div class="abs nav-item" style="left:556px;width:179px">
    <svg width="18" height="17" viewBox="0 0 18 17"><path d="M9 15S1 10 1 5a4 4 0 0 1 8-1 4 4 0 0 1 8 1c0 5-8 10-8 10z" fill="#333"/></svg>CHARITY</div>
  <div class="abs nav-item" style="left:735px;width:193px">
    <svg width="13" height="18" viewBox="0 0 13 18"><path d="M6.5 17S1 10 1 6.5a5.5 5.5 0 0 1 11 0C12 10 6.5 17 6.5 17z" fill="none" stroke="#333" stroke-width="1.8"/><circle cx="6.5" cy="6.5" r="2" fill="#333"/></svg>LOCATIONS</div>
  <div class="abs nav-item last" style="left:928px;width:182px">
    <svg width="15" height="17" viewBox="0 0 15 17"><path d="M3 1l3 4-2 2c1 3 3 5 5 6l2-2 3 3-2 2C6 16 0 9 1 3z" fill="#333"/></svg>CONTACT</div>
</nav>

<!-- hero -->
<section class="abs hero">
  <div class="abs hero-bride" role="img" aria-label="Sepia photo of a smiling bride in a strapless wedding gown"></div>
  <div class="abs hero-rings" role="img" aria-label="Two silver diamond engagement rings standing on a white surface"></div>
  <h1 class="abs hero-title">WEDDING COLLECTION</h1>
  <p class="abs hero-sub">a handmade jewelry for every women</p>
  <div class="abs btn-hero">SHOP NOW</div>
  <div class="abs dot" style="top:365px"></div>
  <div class="abs dot" style="top:392px"></div>
  <div class="abs dot on" style="top:419px"></div>
  <div class="abs dot" style="top:446px"></div>
</section>

<!-- popular products -->
<h2 class="abs sec-title" style="top:700px">POPULAR PRODUCTS</h2>
<svg class="abs ornament" style="top:735px" viewBox="0 0 210 20"><line x1="0" y1="10" x2="70" y2="10" stroke="#777" stroke-width="1.5"/><line x1="140" y1="10" x2="210" y2="10" stroke="#777" stroke-width="1.5"/><ellipse cx="105" cy="10" rx="32" ry="7" fill="var(--accent)" opacity=".75"/></svg>

<div class="abs card-img" style="left:99px;top:777px;background:
  radial-gradient(ellipse 90px 80px at 50% 72%,#8a5a3c 0%,#9b6a4b 55%,rgba(155,106,75,0) 100%),
  radial-gradient(ellipse 120px 110px at 50% 45%,#fdfdfd 0%,#ececec 60%,rgba(236,236,236,0) 100%),
  radial-gradient(ellipse 45px 60px at 50% 14%,#3a2c25 0%,rgba(58,44,37,0) 100%),
  linear-gradient(180deg,#f4f4f4,#efefef)" role="img" aria-label="Model in a white blouse and brown suede shorts"></div>
<div class="abs tag orange" style="left:106px;top:774px">NEW</div>
<div class="abs card-img" style="left:442px;top:777px;background:
  radial-gradient(ellipse 130px 120px at 45% 72%,#6e655e 0%,#8f857d 50%,rgba(143,133,125,0) 100%),
  radial-gradient(ellipse 120px 140px at 55% 28%,#d2c8c0 0%,#b9aea6 60%,rgba(185,174,166,0) 100%),
  linear-gradient(180deg,#e6e1dd,#cfc8c2)" role="img" aria-label="Model wearing statement earrings, layered necklace and cuff bracelet"></div>
<div class="abs tag orange" style="left:686px;top:774px">SALE</div>
<div class="abs card-img" style="left:785px;top:777px;background:
  radial-gradient(ellipse 110px 170px at 50% 58%,#3a3a3a 0%,#6d6d6d 45%,rgba(109,109,109,0) 100%),
  radial-gradient(ellipse 50px 60px at 50% 12%,#d9c28a 0%,rgba(217,194,138,0) 100%),
  linear-gradient(180deg,#f5f5f5,#ececec)" role="img" aria-label="Model in a black and white striped belted dress"></div>
<div class="abs tag dark" style="left:1026px;top:774px">NEW</div>

<div class="abs arrow" style="left:83px;top:1000px"><svg width="10" height="12" viewBox="0 0 10 12"><path d="M8 1 3 6l5 5" fill="none" stroke="#fff" stroke-width="2"/></svg></div>
<div class="abs arrow" style="left:1083px;top:1000px"><svg width="10" height="12" viewBox="0 0 10 12"><path d="M2 1l5 5-5 5" fill="none" stroke="#fff" stroke-width="2"/></svg></div>

<div class="abs card-name" style="left:99px;top:1242px">D Black Jacket - Young</div>
<div class="abs card-price" style="left:99px;top:1262px">$ 45.00</div>
<div class="abs card-btn" style="left:210px;top:1285px">SHOP NOW</div>
<div class="abs card-name" style="left:442px;top:1242px">D Black Jacket - Young</div>
<div class="abs card-price" style="left:442px;top:1262px">$ 45.00</div>
<div class="abs card-btn" style="left:553px;top:1285px">SHOP NOW</div>
<div class="abs card-name" style="left:785px;top:1242px">D Black Jacket - Young</div>
<div class="abs card-price" style="left:785px;top:1262px">$ 45.00</div>
<div class="abs card-btn" style="left:896px;top:1285px">SHOP NOW</div>

<!-- promo banners -->
<div class="abs promo" style="left:99px;width:469px">
  <div class="abs promo-img" style="background:
    radial-gradient(ellipse 80px 90px at 60% 40%,#d9c3ac 0%,#a78a70 55%,rgba(167,138,112,0) 100%),
    linear-gradient(135deg,#4e3f33,#8b735f)" role="img" aria-label="Sepia portrait of a woman with voluminous hair"></div>
  <div class="abs promo-kicker">WOMEN'S</div>
  <div class="abs promo-big">LIVE STYLE</div>
  <div class="abs promo-small">LOREM IPSUM</div>
</div>
<div class="abs promo" style="left:600px;width:500px">
  <div class="abs promo-img" style="background:
    radial-gradient(circle 14px at 52% 62%,#c9a25a 0%,#b48a45 60%,rgba(180,138,69,0) 100%),
    radial-gradient(ellipse 110px 90px at 50% 60%,#e9dfd5 0%,#cdbfb1 70%,rgba(205,191,177,0) 100%),
    linear-gradient(135deg,#a89888,#ddd2c6)" role="img" aria-label="Close-up of a delicate gold pendant necklace"></div>
  <div class="abs promo-kicker">COLLECTION</div>
  <div class="abs promo-big">JEWELRY</div>
  <div class="abs promo-small">FOR WOMEN'S</div>
</div>

<!-- best seller -->
<h2 class="abs sec-title" style="top:1605px">BEST SELLER</h2>
<svg class="abs ornament" style="top:1641px" viewBox="0 0 210 20"><line x1="0" y1="10" x2="70" y2="10" stroke="#777" stroke-width="1.5"/><line x1="140" y1="10" x2="210" y2="10" stroke="#777" stroke-width="1.5"/><ellipse cx="105" cy="10" rx="32" ry="7" fill="var(--accent)" opacity=".75"/></svg>

<div class="abs card-img" style="left:99px;top:1683px;background:
  radial-gradient(ellipse 70px 170px at 48% 52%,#9a9590 0%,#c9c5c1 50%,rgba(201,197,193,0) 100%),
  linear-gradient(180deg,#f6f6f6,#ececec)" role="img" aria-label="Ink illustration of a hawk perched on a stump"></div>
<div class="abs card-img" style="left:442px;top:1683px;background:
  radial-gradient(circle 50px at 25% 17%,#e8e2da 0%,#7fb3b3 70%,rgba(127,179,179,0) 100%),
  radial-gradient(ellipse 50px 130px at 25% 66%,#c79a6a 0%,rgba(199,154,106,0) 100%),
  radial-gradient(ellipse 80px 140px at 68% 62%,#8a7a6a 0%,#b3a493 55%,rgba(179,164,147,0) 100%),
  linear-gradient(180deg,#f5f5f5,#ececec)" role="img" aria-label="Wall clock, table lamp and checkered side table"></div>
<div class="abs tag orange" style="left:686px;top:1680px">SALE</div>
<div class="abs card-img" style="left:785px;top:1683px;background:
  radial-gradient(ellipse 140px 80px at 50% 55%,#e3a43c 0%,#c98e35 45%,rgba(201,142,53,0) 100%),
  radial-gradient(ellipse 150px 40px at 45% 68%,#4a4a4a 0%,rgba(74,74,74,0) 100%),
  linear-gradient(180deg,#f6f6f6,#efefef)" role="img" aria-label="Wooden office desk set with chairs and cabinets"></div>
<div class="abs tag dark" style="left:1026px;top:1680px">NEW</div>

<div class="abs arrow" style="left:83px;top:1897px"><svg width="10" height="12" viewBox="0 0 10 12"><path d="M8 1 3 6l5 5" fill="none" stroke="#fff" stroke-width="2"/></svg></div>
<div class="abs arrow" style="left:1083px;top:1897px"><svg width="10" height="12" viewBox="0 0 10 12"><path d="M2 1l5 5-5 5" fill="none" stroke="#fff" stroke-width="2"/></svg></div>

<div class="abs card-name" style="left:99px;top:2149px">Lorem Ipsum Dummy</div>
<div class="abs card-price" style="left:99px;top:2169px">$ 45.00</div>
<div class="abs card-btn" style="left:210px;top:2191px">SHOP NOW</div>
<div class="abs card-name" style="left:442px;top:2149px">Lorem Ipsum Dummy</div>
<div class="abs card-price" style="left:442px;top:2169px">$ 45.00</div>
<div class="abs card-btn" style="left:553px;top:2191px">SHOP NOW</div>
<div class="abs card-name" style="left:785px;top:2149px">Lorem Ipsum Dummy</div>
<div class="abs card-price" style="left:785px;top:2169px">$ 45.00</div>
<div class="abs card-btn" style="left:896px;top:2191px">SHOP NOW</div>

<!-- features -->
<section class="abs features">
  <svg class="abs" style="left:108px;top:30px" width="78" height="44" viewBox="0 0 78 44">
    <line x1="0" y1="12" x2="14" y2="12" stroke="var(--accent)" stroke-width="3"/>
    <line x1="4" y1="20" x2="14" y2="20" stroke="var(--accent)" stroke-width="3"/>
    <line x1="8" y1="28" x2="14" y2="28" stroke="var(--accent)" stroke-width="3"/>
    <rect x="16" y="4" width="38" height="28" rx="2" fill="var(--accent)"/>
    <path d="M56 12h12l8 10v10H56z" fill="var(--accent)"/>
    <circle cx="28" cy="36" r="6" fill="var(--accent)" stroke="var(--band)" stroke-width="2"/>
    <circle cx="64" cy="36" r="6" fill="var(--accent)" stroke="var(--band)" stroke-width="2"/>
  </svg>
  <div class="abs feat-text" style="left:211px">FREE SHIPPING WORLDWIDE</div>
  <div class="abs feat-div"></div>
  <svg class="abs" style="left:655px;top:22px" width="58" height="58" viewBox="0 0 58 58" role="img" aria-label="Satisfaction seal">
    <circle cx="29" cy="29" r="27" fill="#d9a21e"/>
    <circle cx="29" cy="29" r="19" fill="#2a2a2a"/>
  </svg>
  <div class="abs feat-text" style="left:770px">100% CLIENT SATISFACTION</div>
</section>

<!-- footer -->
<footer class="abs footer">
  <div class="abs f-head" style="left:98px">Contact Us</div>
  <ul class="abs f-list" style="left:98px">
    <li>Tide Harbor Shop</li>
    <li>18/40 Quay Street, Harbor City, USA</li>
    <li>hello@tideharbor.example</li>
    <li>http://tideharbor.example</li>
    <li>Tell: 1-100-555-0142</li>
  </ul>
  <div class="abs f-head" style="left:398px">Quick Links</div>
  <ul class="abs f-list" style="left:398px">
    <li>Cart</li><li>Checkout</li><li>My Account</li><li>Wishlist</li>
  </ul>
  <div class="abs f-head" style="left:621px">Customer Care</div>
  <ul class="abs f-list" style="left:621px">
    <li>Customer Service</li><li>Track My Order</li><li>Contact US</li>
  </ul>
  <div class="abs f-head" style="left:872px">Newsletter Signup</div>
  <p class="abs f-note">Subscribe to stay get update from Tide Harbor</p>
  <div class="abs f-input">Email</div>
  <div class="abs f-send"><svg width="22" height="20" viewBox="0 0 22 20"><path d="M1 9 21 1l-6 18-4-7z" fill="#fff"/><path d="M11 12 21 1" stroke="var(--accent)" stroke-width="1.5"/></svg></div>
</footer>
<div class="abs base">
  <div class="abs copy">TIDE HARBOR 7 © 2016 Privacy policy</div>
  <div class="abs social" style="left:986px" role="img" aria-label="Social profile link"></div>
  <div class="abs social" style="left:1018px" role="img" aria-label="Social profile link"></div>
  <div class="abs social" style="left:1050px" role="img" aria-label="Social profile link"></div>
  <div class="abs social" style="left:1082px" role="img" aria-label="Social profile link"></div>
</div>

</body>
</html>
```